Brand new redesign of Brightwell finance website

I need a new website design that i can advertise a great low interest rate on the front page and capture input application details that will send through to my email address.

some car finance companies will be similar to this would be listed below

quorvaloans.com.au
pelmarfinance.com.au
finance715.com.au
gundrelfinance.com.au
finance93.com.au
Updates

Project Deadline Extended
Reason: I have changed the project to a committed project. all the webpages should have the same format just different content and i want to be able to edit the front page easily to update my interest rates.

Project Deadline Extended
Reason: Provide more time for resubmission and submission work

Target Market(s)

Australian Finance market targeting a younger demographic

Industry/Entity Type

Finance

Coding

Coded - Design and coding required

Number of Pages Required

5+ page

Font styles to use
Serif
Sans Serif

Colors
0255a3
ffffff
cedeed

Requirements
Must have
• application capture form
• apply now buttons
• Headline rate front page

```html
<!DOCTYPE html>
<html lang="en">
<head>
<meta charset="utf-8">
<title>Brightwell Finance</title>
<link href="https://fonts.googleapis.com/css2?family=Open+Sans:wght@400;600;700&family=Alegreya:wght@400;700&display=swap" rel="stylesheet">
<style>
:root{
  --brand:#2b3990;
  --brand-blue:#0255a3;
  --ice:#cedeed;
  --ink:#222;
  --text:#444;
  --muted:#888;
  --rule:#1f7fa8;
  --white:#fff;
  --grey-band:#e6e6e6;
  --soft-band:#f3f5f8;
  --footer:#232a36;
  --footer-text:#c9ced6;
  --field:#e4e4e4;
}
*{box-sizing:border-box;margin:0;padding:0}
html,body{width:1200px;height:2765px;overflow:hidden}
body{position:relative;font-family:"Open Sans",Arial,sans-serif;color:var(--text);background:var(--white)}
.abs{position:absolute}

/* header */
.site-header{left:0;top:0;width:1200px;height:136px;background:linear-gradient(90deg,#fff 40%,#eef6fb)}
.brand{left:92px;top:40px;display:flex;align-items:center;gap:12px}
.brand-dot{width:46px;height:46px;border-radius:50%;background:var(--brand)}
.brand-name{font-weight:700;font-size:24px;color:var(--brand);line-height:1}
.search{left:755px;top:26px;width:203px;height:34px;border:1px solid #cfcfcf;border-radius:17px;background:#fff;font-size:11px;color:#aaa;padding:9px 16px}
.search svg{position:absolute;right:12px;top:9px}
.social-top{left:985px;top:34px;display:flex;gap:22px}
.social-top span{width:16px;height:16px;border-radius:50%;background:#222}
.main-nav{left:455px;top:90px;display:flex;gap:30px;font-size:13.5px;font-weight:600;color:#222}
.main-nav .active{color:var(--brand-blue)}

/* hero */
.hero{left:0;top:136px;width:1200px;height:568px;background:linear-gradient(180deg,#3f8fd8 0%,#8cc3ec 38%,#b7d58a 62%,#6f9a3c 100%)}
.hero-card{left:90px;top:332px;width:531px;height:248px;background:var(--white);padding:32px 18px}
.hero-card h1{font-size:34px;font-weight:700;color:var(--brand);letter-spacing:.3px}
.hero-card h2{font-size:29px;font-weight:400;color:#222;margin-top:6px}
.hero-card p{font-size:13.5px;line-height:24px;margin-top:22px;color:#333}
.apply-form{left:769px;top:223px;width:339px;height:435px;background:var(--white);border-radius:6px;padding:18px 28px}
.apply-form h3{font-size:30px;font-weight:600;color:#2a2a2a;letter-spacing:.5px}
.apply-form label{display:block;font-size:10.5px;font-weight:700;color:#222;margin-top:16px}
.apply-form .field{height:38px;margin-top:10px;background:var(--field);border:1px solid #d3d3d3;border-radius:6px;box-shadow:inset 0 2px 4px rgba(0,0,0,.12)}
.apply-form .submit{display:block;margin:22px auto 0;width:128px;height:42px;border-radius:6px;background:var(--brand);color:#fff;font-size:13px;font-weight:600;text-align:center;line-height:42px}

/* welcome */
.welcome{left:0;top:757px;width:1200px;text-align:center}
.welcome h2{font-size:40px;font-weight:700;color:#2a2a2a}
.welcome h2 span{color:var(--brand)}
.welcome p{width:840px;margin:22px auto 0;font-size:14px;line-height:24px;color:#333}
.feature{top:944px;width:230px;text-align:center}
.feature-icon{width:128px;height:128px;margin:0 auto;border:1px solid #d6d6d6;border-radius:50%;display:flex;align-items:center;justify-content:center}
.feature h4{font-size:11px;font-weight:400;color:#222;margin-top:32px}
.feature p{font-size:11px;line-height:20px;color:#333;margin-top:2px}

/* services intro */
.services-intro{left:0;top:1242px;width:1150px;height:85px;background:var(--soft-band)}
.services-intro h3{position:absolute;right:798px;top:14px;text-align:right;font-size:22px;font-weight:700;color:#222;line-height:28px;letter-spacing:.5px}
.services-intro .bar{position:absolute;left:398px;top:14px;width:3px;height:58px;background:var(--rule)}
.services-intro p{position:absolute;left:440px;top:10px;width:690px;font-size:13px;line-height:22px;font-style:italic;color:#999}

/* service tiles */
.services{left:0;top:1373px;width:1200px;height:527px;background:var(--grey-band)}
.tile{width:315px;height:223px;border:3px solid #fff;box-shadow:0 1px 3px rgba(0,0,0,.15)}
.tile-label{position:absolute;left:50%;top:50%;transform:translate(-50%,-50%);background:rgba(40,40,40,.72);color:#fff;font-size:26px;white-space:nowrap;padding:8px 26px;min-width:230px;text-align:center}
.tile.car{background:linear-gradient(135deg,#5f7d54,#1f4f9e 60%,#2b2b2b)}
.tile.home{background:linear-gradient(135deg,#5a8a2a,#b8a084 60%,#e2c4a6)}
.tile.personal{background:linear-gradient(180deg,#8cc8e8,#e6ecef 55%,#cbb8a0)}
.tile.insurance{background:linear-gradient(180deg,#4f84c8,#9cc3e6 55%,#6f9a3c)}
.tile.property{background:linear-gradient(160deg,#4d7fc4,#9db6cf 50%,#3f4f62)}
.tile.other{background:linear-gradient(180deg,#3f6aa8,#c46a3a 60%,#2e5aa0)}

/* faq */
.faq{left:101px;top:1960px;width:470px;font-family:"Alegreya",Georgia,serif}
.faq h3{font-size:25px;font-weight:700;color:#111}
.faq .underline{width:66px;height:1px;background:#ccc;margin-top:12px;position:relative}
.faq .underline::after{content:"";position:absolute;left:22px;top:-4px;width:8px;height:8px;border-radius:50%;background:var(--brand)}
.faq-item{position:absolute;left:0;font-size:20px;color:#222;padding-left:20px;white-space:nowrap}
.faq-item::before{content:"";position:absolute;left:0;top:10px;width:3px;height:3px;border-radius:50%;background:#ccc}
.faq-answer{position:absolute;left:20px;top:2178px;width:470px;font-family:"Open Sans",Arial,sans-serif;font-size:12px;line-height:20px;color:#999}
.team-grid{left:614px;top:1966px;width:490px;height:402px;display:grid;grid-template-columns:326px 162px;grid-template-rows:200px 200px;gap:2px}
.team-grid div{background:linear-gradient(135deg,#8a8f98,#cfd4da)}
.team-grid div:nth-child(2){background:linear-gradient(135deg,#6e8aa8,#dfe6ee)}
.team-grid div:nth-child(3){background:linear-gradient(135deg,#b8bcc2,#e9ecef)}
.team-grid div:nth-child(4){background:linear-gradient(135deg,#7d8ea3,#d6e2ee)}

/* footer */
.site-footer{left:0;top:2457px;width:1200px;height:308px;background:var(--footer);color:var(--footer-text)}
.foot-col{top:60px}
.foot-col h4{font-size:20px;font-weight:600;color:#fff}
.foot-col h4::after{content:"";display:block;width:28px;height:2px;background:var(--rule);margin-top:10px}
.foot-col p{font-size:11.5px;line-height:19px;margin-top:14px;width:230px}
.foot-col ul{list-style:none;margin-top:8px}
.foot-col li{font-size:11.5px;line-height:30px;padding-left:18px;position:relative}
.foot-col li::before{content:"";position:absolute;left:0;top:11px;width:5px;height:5px;border-right:1.5px solid var(--rule);border-bottom:1.5px solid var(--rule);transform:rotate(-45deg)}
.contact-row{display:flex;gap:14px;font-size:11.5px;line-height:19px;margin-top:10px}
.contact-row svg{flex:none;margin-top:3px}
.social-foot{left:101px;top:2690px;display:flex;gap:18px}
.social-foot span{width:30px;height:30px;border-radius:50%;background:#323a48}
</style>
</head>
<body>

<header class="site-header abs">
  <div class="brand abs" style="position:absolute"><span class="brand-dot"></span><span class="brand-name">Brightwell Finance</span></div>
  <div class="search abs">Search
    <svg width="14" height="14" viewBox="0 0 14 14"><circle cx="6" cy="6" r="4.5" fill="none" stroke="#666" stroke-width="1.5"/><line x1="9.5" y1="9.5" x2="13" y2="13" stroke="#666" stroke-width="1.5"/></svg>
  </div>
  <div class="social-top abs"><span></span><span></span><span></span><span></span></div>
  <nav class="main-nav abs">
    <span class="active">Home</span><span>Home Loans</span><span>Motor Loans</span><span>Calculators</span><span>About F93</span><span>Blog</span><span>Contact Us</span>
  </nav>
</header>

<section class="hero abs" role="img" aria-label="Family playing in a sunny green meadow under a blue sky"></section>
<div class="hero-card abs">
  <h1>GREAT LOW INTEREST RATE</h1>
  <h2>MORBI NON LIBERO LIGULA</h2>
  <p>Quisque non nibh ut ipsum fringilla maximus. In molestie f posuere<br>Pellentesque purus dui, faucibus cursus venenatis nec, alit ac diam<br>Maecenas consectetur libero eu</p>
</div>
<form class="apply-form abs">
  <h3>LET'S GET STARTED</h3>
  <label>LOAN AMOUNT :</label><div class="field"></div>
  <label>DEPOSIT (IF ANY) :</label><div class="field"></div>
  <label>PURPOSE OF LOAN :</label><div class="field"></div>
  <label>POST CODE :</label><div class="field"></div>
  <span class="submit">SUBMIT</span>
</form>

<section class="welcome abs">
  <h2>WELCOME TO <span>BRIGHTWELL</span></h2>
  <p>Quisque non nibh ut ipsum fringilla maximus. In molestie feugiat eros et posuere. Pellentesque purus dui, faucibus cursus venenatis nec, aliquet ac diam. Maecenas consectetur libero eu risus tristique, et rutrum justo efficitur.</p>
</section>

<div class="feature abs" style="left:95px">
  <div class="feature-icon"><svg width="60" height="60" viewBox="0 0 60 60" fill="none" stroke="#333" stroke-width="2.5"><path d="M20 34a14 14 0 1 1 20 0c-3 3-4 5-4 8H24c0-3-1-5-4-8z"/><line x1="24" y1="47" x2="36" y2="47"/><line x1="26" y1="52" x2="34" y2="52"/><text x="30" y="31" text-anchor="middle" font-size="16" font-family="Open Sans,sans-serif" fill="#333" stroke="none" font-weight="700">$</text><line x1="4" y1="24" x2="10" y2="24"/><line x1="50" y1="24" x2="56" y2="24"/><line x1="10" y1="8" x2="14" y2="12"/><line x1="50" y1="8" x2="46" y2="12"/></svg></div>
  <h4>QUISQUE NON NIBHIPSUM</h4>
  <p>fringimus molestie feugiat eros et posuere. Maecenas consectetur libero eu risus tristir pellentesque sapien</p>
</div>
<div class="feature abs" style="left:351px">
  <div class="feature-icon"><svg width="60" height="60" viewBox="0 0 60 60"><path d="M27 10a22 22 0 1 0 22 22H27z" fill="none" stroke="#555" stroke-width="4"/><path d="M32 5v22h22A22 22 0 0 0 32 5z" fill="#555"/></svg></div>
  <h4>AUISQUE NON NIBHIPSUM</h4>
  <p>fringimus molestie feugiat eros et posuere. Maecenas consectetur libero eu risus tristir pellentesque sapien</p>
</div>
<div class="feature abs" style="left:609px">
  <div class="feature-icon"><svg width="60" height="60" viewBox="0 0 60 60" fill="#333"><rect x="8" y="24" width="10" height="14"/><path d="M18 24l24-12v38L18 38z"/><rect x="20" y="38" width="7" height="12"/><path d="M46 24a8 8 0 0 1 0 12" fill="none" stroke="#333" stroke-width="3"/></svg></div>
  <h4>SUISQUE NON NIBHIPSUM</h4>
  <p>fringimus molestie feugiat eros et posuere. Maecenas consectetur libero eu risus tristir pellentesque sapien</p>
</div>
<div class="feature abs" style="left:867px">
  <div class="feature-icon"><svg width="64" height="64" viewBox="0 0 64 64" fill="#444"><path d="M4 26l10-6 6 14-10 6z"/><path d="M60 26l-10-6-6 14 10 6z"/><path d="M18 24l10-4 8 2 10-2 4 12-12 12-4-2-4 2-4-2-4-2-6-6z"/></svg></div>
  <h4>WUISQUE NON NIBHIPSUM</h4>
  <p>fringimus molestie feugiat eros et posuere. Maecenas consectetur libero eu risus tristir pellentesque sapien</p>
</div>

<section class="services-intro abs">
  <h3>WE OFFER<br>DIFFERENT SERVICES</h3>
  <span class="bar"></span>
  <p>Duis aute irure dolor in reprehenderit in voluptate velit esse cillum dolore eu fugiat nulla pariatur. Excepteur sint occaecat cupidatat non proident, sunt in culpa qui officia deserunt mollit anim id est laborum. Consect petur adipiscing elit.</p>
</section>

<section class="services abs">
  <div class="tile car abs" style="left:92px;top:18px" role="img" aria-label="Blue car driving along a road"><span class="tile-label">CAR LOAN</span></div>
  <div class="tile home abs" style="left:444px;top:18px" role="img" aria-label="Small model house held in an open hand"><span class="tile-label">HOME LOAN</span></div>
  <div class="tile personal abs" style="left:794px;top:18px" role="img" aria-label="Family walking on a tropical beach"><span class="tile-label">PERSONAL LOAN</span></div>
  <div class="tile insurance abs" style="left:92px;top:278px" role="img" aria-label="Person holding an umbrella over someone working on a laptop in a field"><span class="tile-label">INSURANCES</span></div>
  <div class="tile property abs" style="left:444px;top:278px" role="img" aria-label="Glass office towers against a blue sky"><span class="tile-label">PROPERTY LOAN</span></div>
  <div class="tile other abs" style="left:794px;top:278px" role="img" aria-label="Rows of colourful stadium seats"><span class="tile-label">OTHER</span></div>
</section>

<section class="faq abs">
  <h3>Frequently Asked Questions</h3>
  <div class="underline"></div>
  <div class="faq-item" style="top:80px">How can i get financial aid to live off campus?</div>
  <div class="faq-item" style="top:145px">Does Harlowell share my information with others?</div>
  <div class="faq-answer" style="top:182px;left:20px">Neque porro quisquam est, qui dolorem ipsum quia dolor sit amet, consectetur, adipisci velit, sed quia non numquam eius modi tempora incidunt ut labore et dolore magnam aliquam quaerat voluptatem Harlowell porro amet sed quia labour ipsum incidunt ut porro.</div>
  <div class="faq-item" style="top:305px">Can i make a payments at the nearest your center?</div>
  <div class="faq-item" style="top:368px">How do i link multiple accounts with my profile?</div>
  <div class="faq-item" style="top:432px">What kind of financial advice do you give?</div>
</section>
<div class="team-grid abs" role="img" aria-label="Collage of business people meeting and working in an office">
  <div></div><div></div><div></div><div></div>
</div>

<footer class="site-footer abs">
  <div class="foot-col abs" style="left:101px">
    <h4>About Us</h4>
    <p>Lorem ipsum dolor sit amet, consectetur adipiscing elit. Curabitur pellentesque neque eget diam posuere porta.</p>
  </div>
  <div class="foot-col abs" style="left:354px">
    <h4>Contact Info</h4>
    <div class="contact-row"><svg width="10" height="13" viewBox="0 0 10 13"><path d="M5 0a5 5 0 0 0-5 5c0 4 5 8 5 8s5-4 5-8a5 5 0 0 0-5-5z" fill="var(--rule)"/><circle cx="5" cy="5" r="1.8" fill="var(--footer)"/></svg><span>41 Larkmoor Lane<br>Castrel 30417,<br>Aldemere</span></div>
    <div class="contact-row"><svg width="12" height="12" viewBox="0 0 12 12"><path d="M2 0l3 3-1.5 2a7 7 0 0 0 3.5 3.5L9 7l3 3-2 2C5 12 0 7 0 2z" fill="var(--rule)"/></svg><span>(800) 555-0142</span></div>
    <div class="contact-row"><svg width="13" height="10" viewBox="0 0 13 10"><rect width="13" height="10" fill="var(--rule)"/><path d="M0 0l6.5 5L13 0" fill="none" stroke="var(--footer)" stroke-width="1.2"/></svg><span>info@brightwell.com</span></div>
    <div class="contact-row"><svg width="12" height="12" viewBox="0 0 12 12"><circle cx="6" cy="6" r="5" fill="none" stroke="var(--rule)" stroke-width="2"/><path d="M6 3v3h2" fill="none" stroke="var(--rule)" stroke-width="1.4"/></svg><span>Mon - Sat 09:00 - 17:00</span></div>
  </div>
  <div class="foot-col abs" style="left:610px">
    <h4>Our Services</h4>
    <ul><li>Life Insurance</li><li>Car Insurance</li><li>Travel Insurance</li><li>House Insurance</li><li>Vehicle Insurance</li><li>Boat Insurance</li></ul>
  </div>
  <div class="foot-col abs" style="left:864px">
    <h4>Additional Links</h4>
    <ul><li>Our Company</li><li>Our Team</li><li>Our Partners</li><li>Careers</li><li>Contact Us</li></ul>
  </div>
</footer>
<div class="social-foot abs"><span></span><span></span><span></span><span></span></div>

</body>
</html>
```